Tooth Fairy Certificates with a Brown Tooth Fairy character on it (animation)
Tooth Certificate
I needs a name and date slot
also boxes for checks or stars next to each word
- clean
- shiny
- needs more brushing

Great Job, I'm so Proud of you! keep up the great brushing!

I need 4 per 11x8 page or 2- 5' 7 per page.

```html
<!DOCTYPE html>
<html lang="en">
<head>
<meta charset="utf-8">
<title>Tooth Fairy Certificate</title>
<link rel="stylesheet" href="https://fonts.googleapis.com/css2?family=Montserrat:wght@800&family=Oranienbaum&family=Indie+Flower&family=Tinos&display=swap">
<style>
  :root {
    --frame: #a48bb0;
    --paper: #efe0ef;
    --cloud-pink: #bf78b5;
    --cloud-blue: #b7dbe6;
    --banner: #6e2a6f;
    --line: #b47ab8;
    --box: #5b2a6a;
    --ink: #1e1a1e;
    --message: #2c2466;
    --white: #ffffff;
    --star-blue: #2aa7d8;
    --star-navy: #1f64a8;
    --star-yellow: #f5e62a;
    --tooth: #fbfbfd;
    --fairy-dress: #c6a3d6;
    --fairy-wing: #8f85b8;
  }
  html, body {
    margin: 0;
    padding: 0;
    width: 1200px;
    height: 872px;
    overflow: hidden;
    background: var(--frame);
  }
  .certificate {
    position: relative;
    width: 1200px;
    height: 872px;
    background: var(--frame);
  }
  .certificate__paper {
    position: absolute;
    left: 33px;
    top: 24px;
    right: 33px;
    bottom: 24px;
    background: var(--paper);
  }
  .art {
    position: absolute;
  }
  .art--clouds {
    left: 263px;
    top: 49px;
    width: 590px;
    height: 182px;
    border-radius: 90px 90px 40px 40px;
    background: linear-gradient(100deg, var(--cloud-pink) 0%, var(--cloud-pink) 62%, var(--cloud-blue) 100%);
  }
  .title {
    position: absolute;
    left: 263px;
    top: 152px;
    width: 500px;
    margin: 0;
    text-align: center;
    font-family: "Montserrat", sans-serif;
    font-weight: 800;
    font-size: 44px;
    color: var(--white);
    letter-spacing: 0.5px;
  }
  .banner {
    position: absolute;
    left: 191px;
    top: 244px;
    width: 705px;
    height: 96px;
    background: var(--banner);
    border-radius: 10px;
    display: flex;
    align-items: center;
    justify-content: center;
    font-family: "Oranienbaum", serif;
    font-size: 39px;
    color: var(--white);
  }
  .field {
    position: absolute;
    left: 213px;
    display: flex;
    align-items: flex-end;
    font-family: "Oranienbaum", serif;
    font-size: 50px;
    color: var(--ink);
    line-height: 1;
  }
  .field--name { top: 354px; }
  .field--date { top: 416px; }
  .field__label { width: 140px; }
  .field__colon { width: 27px; }
  .field__line {
    width: 418px;
    height: 3px;
    background: var(--line);
    margin-bottom: 4px;
  }
  .checklist {
    position: absolute;
    left: 213px;
    top: 488px;
    margin: 0;
    padding: 0;
    list-style: none;
  }
  .checklist__item {
    display: flex;
    align-items: center;
    height: 50px;
    margin-bottom: 11px;
    font-family: "Indie Flower", cursive;
    font-size: 52px;
    line-height: 1;
    color: var(--ink);
  }
  .checklist__box {
    flex: none;
    width: 48px;
    height: 48px;
    border: 3px solid var(--box);
    margin-right: 22px;
    box-sizing: border-box;
  }
  .message {
    position: absolute;
    left: 0;
    right: 0;
    top: 689px;
    margin: 0;
    text-align: center;
    font-family: "Tinos", serif;
    font-size: 47px;
    line-height: 56px;
    color: var(--message);
  }
  .art--fairy {
    left: 797px;
    top: 24px;
    width: 356px;
    height: 343px;
    background: linear-gradient(160deg, var(--fairy-wing) 0%, var(--fairy-dress) 60%, var(--paper) 100%);
    border-radius: 40% 40% 30% 30%;
    opacity: 0.85;
  }
  .art--tooth {
    background: var(--tooth);
    border-radius: 40% 40% 45% 45%;
  }
  .art--tooth-top { left: 56px; top: 66px; width: 90px; height: 90px; }
  .art--teeth-bottom { left: 87px; top: 726px; width: 173px; height: 87px; }
  .art--tooth-right { left: 973px; top: 707px; width: 107px; height: 107px; }
  .art--star { border-radius: 50%; }
  .art--star-a { left: 180px; top: 120px; width: 50px; height: 50px; background: var(--star-blue); }
  .art--star-b { left: 335px; top: 94px; width: 44px; height: 44px; background: var(--star-blue); }
  .art--star-c { left: 230px; top: 183px; width: 58px; height: 58px; background: var(--star-navy); }
  .art--star-d { left: 770px; top: 235px; width: 36px; height: 36px; background: var(--star-yellow); }
  .art--star-e { left: 1032px; top: 705px; width: 42px; height: 42px; background: var(--cloud-blue); }
</style>
</head>
<body>
<main class="certificate">
  <div class="certificate__paper"></div>

  <div class="art art--clouds" role="img" aria-label="Pink and light blue cartoon clouds behind the title"></div>

  <div class="art art--star art--star-a" role="img" aria-label="Blue star"></div>
  <div class="art art--star art--star-b" role="img" aria-label="Blue star"></div>
  <div class="art art--star art--star-c" role="img" aria-label="Navy star"></div>

  <h1 class="title">THE TOOTH FAIRY</h1>

  <div class="art art--fairy" role="img" aria-label="Brown-skinned tooth fairy in a lavender dress with wings, holding a star wand"></div>
  <div class="art art--star art--star-d" role="img" aria-label="Yellow star on the wand tip"></div>

  <div class="banner">THIS TOOTH CERTIFICATE IS AWARDED TO</div>

  <div class="field field--name">
    <span class="field__label">NAME</span><span class="field__colon">:</span><span class="field__line"></span>
  </div>
  <div class="field field--date">
    <span class="field__label">DATE</span><span class="field__colon">:</span><span class="field__line"></span>
  </div>

  <ul class="checklist">
    <li class="checklist__item"><span class="checklist__box"></span>Clean</li>
    <li class="checklist__item"><span class="checklist__box"></span>Shiny</li>
    <li class="checklist__item"><span class="checklist__box"></span>Needs more brushing</li>
  </ul>

  <p class="message">Great job, I’m so proud of you !!!<br>Keep up the great brushing!!</p>

  <div class="art art--tooth art--tooth-top" role="img" aria-label="Smiling cartoon tooth"></div>
  <div class="art art--tooth art--teeth-bottom" role="img" aria-label="Two smiling cartoon teeth"></div>
  <div class="art art--tooth art--tooth-right" role="img" aria-label="Smiling cartoon tooth"></div>
  <div class="art art--star art--star-e" role="img" aria-label="Light blue star"></div>
</main>
</body>
</html>
```